Supplement Bottle Packaging and Design

We want to rebrand our current health supplements (see below). We do want it to be modern, vibrant and appealing supplement bottles. Very upscale and elegant as it targets primarily women.
NOTE: READ THE ATTACHED WORD DOCUMENT!
Bottle size: We are totally open to the bottle size and shape, as long it's a typical supplement bottle size to handle 90-120 capsules; what we mostly need is new bottle design/packaging. YOU DON’T HAVE TO USE THE CURRENT WHITE BOTTLE SHAPE, BUT ANYTHING MORE MODERN WOULD WORK!
Updates
We need more modern, clean sleek designs to choose from
Look and feel
Each slider illustrates characteristics of the customer's brand and the style your logo design should communicate.

```html
<!DOCTYPE html>
<html lang="en">
<head>
<meta charset="utf-8">
<title>Luma Supplement Labels</title>
<link rel="stylesheet" href="https://fonts.googleapis.com/css2?family=Montserrat:wght@300;400;600;700;800&display=swap">
<style>
  :root {
    --page: #ffffff;
    --ink: #ffffff;
    --ink-soft: rgba(255,255,255,0.85);
    --rule: rgba(255,255,255,0.55);
    --liver: #7a4f97;
    --liver-badge: #5e3a7a;
    --tummy: #d3283c;
    --tummy-badge: #a81d2e;
    --hormone: #5ead46;
    --hormone-badge: #458a33;
    --sugar: #3bb1de;
    --sugar-badge: #2a8fb8;
  }
  * { margin: 0; padding: 0; box-sizing: border-box; }
  html, body {
    width: 1200px; height: 600px; overflow: hidden;
    background: var(--page);
    font-family: "Montserrat", sans-serif;
    color: var(--ink);
  }
  .label-row { position: relative; width: 1200px; height: 600px; }
  .label {
    position: absolute; top: 136px; width: 238px; height: 328px;
    border-radius: 6px; overflow: hidden;
  }
  .label--liver   { left: 108px; background: var(--liver); }
  .label--tummy   { left: 361px; background: var(--tummy); }
  .label--hormone { left: 614px; background: var(--hormone); }
  .label--sugar   { left: 867px; background: var(--sugar); }

  .brand {
    position: absolute; left: 24px; top: 49px; height: 214px;
    writing-mode: vertical-rl; transform: rotate(180deg);
    font-weight: 800; font-size: 50px; line-height: 1;
    letter-spacing: 0.02em; text-align: left;
  }
  .product-name {
    position: absolute; left: 96px; bottom: 151px;
    font-weight: 700; font-size: 21px; line-height: 26px;
    letter-spacing: 0.2em; text-transform: uppercase;
  }
  .label--hormone .product-name { letter-spacing: 0.13em; }
  .rule {
    position: absolute; left: 96px; top: 187px; width: 110px; height: 1px;
    background: var(--rule);
  }
  .tagline {
    position: absolute; left: 96px; top: 193px;
    font-weight: 700; font-size: 7px; line-height: 11px;
    letter-spacing: 0.2em; text-transform: uppercase;
  }
  .count {
    position: absolute; left: 96px; top: 235px;
    display: flex; align-items: center; gap: 5px;
  }
  .count-badge {
    width: 32px; height: 18px; border-radius: 2px;
    display: flex; align-items: center; justify-content: center;
    font-weight: 600; font-size: 10px; letter-spacing: 0.04em;
  }
  .label--liver .count-badge   { background: var(--liver-badge); }
  .label--tummy .count-badge   { background: var(--tummy-badge); }
  .label--hormone .count-badge { background: var(--hormone-badge); }
  .label--sugar .count-badge   { background: var(--sugar-badge); }
  .count-unit {
    font-weight: 400; font-size: 7px; line-height: 9px;
    letter-spacing: 0.2em; color: var(--ink-soft); text-transform: uppercase;
  }
  .supplement-type {
    position: absolute; left: 96px; top: 258px;
    font-weight: 400; font-size: 7.5px; letter-spacing: 0.2em;
    color: var(--ink-soft); text-transform: uppercase;
  }
</style>
</head>
<body>
<main class="label-row">

  <section class="label label--liver">
    <div class="brand">LUMA</div>
    <h2 class="product-name">Liver<br>Luma</h2>
    <div class="rule"></div>
    <p class="tagline">Rejuvenating cleanse<br>&amp; detox formula*</p>
    <div class="count"><span class="count-badge">120</span><span class="count-unit">Vegetable<br>Capsules</span></div>
    <p class="supplement-type">Dietary supplement</p>
  </section>

  <section class="label label--tummy">
    <div class="brand">LUMA</div>
    <h2 class="product-name">Tummy<br>Luma</h2>
    <div class="rule"></div>
    <p class="tagline">Oxygenating<br>colon cleanse*</p>
    <div class="count"><span class="count-badge">90</span><span class="count-unit">Vegetable<br>Capsules</span></div>
    <p class="supplement-type">Dietary supplement</p>
  </section>

  <section class="label label--hormone">
    <div class="brand">LUMA</div>
    <h2 class="product-name">Hormone<br>Luma</h2>
    <div class="rule"></div>
    <p class="tagline">Supports healthy<br>hormone levels*</p>
    <div class="count"><span class="count-badge">60</span><span class="count-unit">Vegetable<br>Capsules</span></div>
    <p class="supplement-type">Dietary supplement</p>
  </section>

  <section class="label label--sugar">
    <div class="brand">LUMA</div>
    <h2 class="product-name">Blood<br>Sugar<br>Luma</h2>
    <div class="rule"></div>
    <p class="tagline">Supports healthy<br>blood glucose levels*</p>
    <div class="count"><span class="count-badge">60</span><span class="count-unit">Vegetable<br>Capsules</span></div>
    <p class="supplement-type">Dietary supplement</p>
  </section>

</main>
</body>
</html>
```